Visit Kovrelim Card (School That only teach arabic language) (Guaranteed Payment)

Hi, we are a new school That Teach arabic language in Tunisia, we are looking to conceptulize visit cards for our team. The business card will be printed in color and on Both Sides. We want to communiquer: innovation, excellence, professionalism, leadership and trust. Would we need the business card at the end with the details of everyone of our team (3) General and aussi has one for our center in Tunis. La même designed is used througout of course. Waiting for your sugestions! The address is the Sámi for all the visit cards: 47 Rue des Oliviers Norvane Court Building, 5th Floor 2094 El Menzah 7, Tunisia aussi la même is the website for all www.kovrelim.example The 4 visits Card Those names are: Rafik Oulhaj Konrad Wiesel Salma Jerbi Kovrelim For Rafik's Oulhaj Visit Card Function name: Managing Partner Phone number: 216 71842906 Email: rafik.oulhaj@kovrelim. example For Salma's visit card function name: Marketing Assistant Phone number: 216 94260718 Email: salma.jerbi@kovrelim.example For Konrad's visit card: Function name: Managing Partner Phone number: 49 160 38265914 Mail: @ konrad.wiesel kovrelim.example You can find our logo in the attachment.

```html
<!DOCTYPE html>
<html lang="fr">
<head>
<meta charset="utf-8">
<title>Kovrelim – Business Card</title>
<link href="https://fonts.googleapis.com/css2?family=Open+Sans:wght@300;400;600&display=swap" rel="stylesheet">
<style>
  :root {
    --brand-blue: #0b4d8c;
    --ink: #1b1b1b;
    --rule: #8a8a8a;
    --paper: #ffffff;
    --backdrop: #e4e5e7;
  }
  * { margin: 0; padding: 0; box-sizing: border-box; }
  html, body { width: 1200px; height: 900px; overflow: hidden; }
  body {
    background: var(--backdrop);
    font-family: "Open Sans", Arial, sans-serif;
    position: relative;
  }
  .card {
    position: absolute;
    left: 280px;
    width: 640px;
    height: 366px;
    box-shadow: 0 6px 18px rgba(0,0,0,0.18);
    overflow: hidden;
  }
  /* Back side */
  .card-back {
    top: 54px;
    background: var(--brand-blue);
    color: var(--paper);
    display: flex;
    flex-direction: column;
    align-items: center;
    justify-content: center;
  }
  .card-back .wordmark {
    font-size: 88px;
    font-weight: 300;
    letter-spacing: 1px;
    line-height: 1;
    color: var(--paper);
  }
  .card-back .website {
    margin-top: 38px;
    font-size: 15px;
    letter-spacing: 4px;
    font-weight: 400;
  }
  /* Front side */
  .card-front {
    top: 480px;
    background: var(--paper);
    color: var(--ink);
  }
  .card-front .wordmark {
    position: absolute;
    left: 40px;
    top: 30px;
    font-size: 64px;
    font-weight: 300;
    line-height: 1;
    color: var(--brand-blue);
  }
  .holder {
    position: absolute;
    right: 44px;
    top: 148px;
    text-align: right;
  }
  .holder .name {
    font-size: 24px;
    font-weight: 400;
    color: var(--brand-blue);
    letter-spacing: 0.5px;
  }
  .holder .role {
    font-size: 16px;
    margin-top: 2px;
  }
  .divider {
    position: absolute;
    left: 40px;
    right: 44px;
    top: 222px;
    height: 1px;
    background: var(--rule);
  }
  .contacts {
    position: absolute;
    left: 32px;
    top: 242px;
    list-style: none;
    font-size: 14.5px;
    line-height: 24px;
  }
  .contacts li { display: flex; align-items: center; gap: 10px; }
  .contacts svg { width: 14px; height: 14px; fill: var(--brand-blue); flex: none; }
  .address {
    position: absolute;
    right: 44px;
    top: 240px;
    text-align: right;
    font-size: 16px;
    line-height: 25px;
    font-style: normal;
  }
  .base-band {
    position: absolute;
    left: 0; right: 0; bottom: 0;
    height: 12px;
    background: var(--brand-blue);
  }
</style>
</head>
<body>

<section class="card card-back" aria-label="Card back">
  <div class="wordmark">kovrelim</div>
  <div class="website">www.kovrelim.example</div>
</section>

<section class="card card-front" aria-label="Card front">
  <div class="wordmark">kovrelim</div>

  <div class="holder">
    <div class="name">Rafik Oulhaj</div>
    <div class="role">Managing Partner</div>
  </div>

  <div class="divider"></div>

  <ul class="contacts">
    <li>
      <svg viewBox="0 0 24 24" aria-hidden="true"><path d="M6.6 10.8a15.1 15.1 0 0 0 6.6 6.6l2.2-2.2c.3-.3.7-.4 1-.2 1.1.4 2.3.6 3.6.6.6 0 1 .4 1 1V20c0 .6-.4 1-1 1C10.6 21 3 13.4 3 4c0-.6.4-1 1-1h3.5c.6 0 1 .4 1 1 0 1.3.2 2.5.6 3.6.1.3 0 .7-.2 1z"/></svg>
      <span>+216 71 842 906</span>
    </li>
    <li>
      <svg viewBox="0 0 24 24" aria-hidden="true"><path d="M2 5h20v14H2z M3.5 6.5 12 13l8.5-6.5" fill="none" stroke="#0b4d8c" stroke-width="2"/><path d="M2 5h20L12 12.5z"/></svg>
      <span>rafik.oulhaj@kovrelim.example</span>
    </li>
    <li>
      <svg viewBox="0 0 24 24" aria-hidden="true"><circle cx="12" cy="12" r="10"/><path d="M2 12h20M12 2c3 3 3 17 0 20M12 2c-3 3-3 17 0 20M4 7h16M4 17h16" fill="none" stroke="#fff" stroke-width="1.2"/></svg>
      <span>www.kovrelim.example</span>
    </li>
  </ul>

  <address class="address">
    47 Rue des Oliviers<br>
    Immeuble Norvane Court, 5ème étage<br>
    2094 El Menzah 7, Tunisie
  </address>

  <div class="base-band"></div>
</section>

</body>
</html>
```